Webdesign für Management Coaching
Zielgruppe
Ich bin Coach/biete Coaching-Leistungen an.
Zielgruppe: Fokus auf Führungskräfte/Entscheider/Management mit technischem Hintergrund (Forschung & Entwicklung, Engineering, Technik, Maschinenbau, Naturwissenschaften)
Coaching-Schwerpunkte: Sinn-Coaching, Begleitung bei Umbrüchen und Veränderungen (privat & beruflich), Sparring & Reflexion
Aufgabenstellung
Gewünscht wurde ein helles Design, das die Logo-Farben aufnimmt. Ausrichtung am Logo & den verwendeten Farben, Schriften
Bilder: Ich werde noch Fotos beim Fotografen machen, die eingebunden werden sollen (Profil, etc.). Bitte Anhaltspunkte nennen, worauf ich die Fotografin hinweisen soll/welche Motive ins Konzept passen.

```html
<!DOCTYPE html>
<html lang="de">
<head>
<meta charset="utf-8">
<title>Christian Wohlgemut Coaching</title>
<link href="https://fonts.googleapis.com/css2?family=EB+Garamond:wght@400;500;600;700&family=Poppins:wght@400;500;600&display=swap" rel="stylesheet">
<style>
:root{
  --slate:#7b9faf;
  --slate-dark:#6a90a3;
  --heading:#6f95a8;
  --ink:#2f3438;
  --muted:#9aa3a8;
  --button-grey:#a9adb0;
  --white:#ffffff;
  --hero-bg:#f4f8f8;
  --star:#ef8f3f;
  --line:#e3e7e9;
}
*{margin:0;padding:0;box-sizing:border-box}
html,body{width:1200px;height:4759px;overflow:hidden}
body{font-family:"EB Garamond",Georgia,serif;color:var(--ink);background:var(--white);position:relative}
section,header,footer{position:absolute;left:0;width:1200px}
.abs{position:absolute}
.eyebrow{font-size:14px;letter-spacing:3.5px;text-transform:uppercase;font-weight:500}
.btn{position:absolute;display:flex;align-items:center;justify-content:center;border-radius:5px;font-size:15px;font-weight:600;color:var(--white);background:var(--slate)}
.photo{position:absolute}

/* Hero */
.hero{top:0;height:764px;background:linear-gradient(160deg,#f6fafa 0%,#f3f7f7 55%,#e4ecee 70%,#ffffff 100%)}
.nav a{position:absolute;top:116px;font-size:15px;font-weight:600;color:var(--slate-dark);text-decoration:none}
.brand-mark{position:absolute;left:526px;top:51px;width:148px;height:148px;border:1px solid var(--slate);border-radius:50%;display:flex;align-items:center;justify-content:center;text-align:center;font-size:15px;font-weight:600;color:var(--slate-dark);line-height:1.2}
.social{position:absolute;top:111px;width:28px;height:28px;border:2px solid var(--slate-dark);border-radius:50%}
.hero h1{position:absolute;left:100px;top:344px;font-size:52px;line-height:56px;font-weight:600;color:var(--heading)}
.hero p{position:absolute;left:100px;top:490px;width:580px;font-size:14px;line-height:23px}
/* About */
.about{top:764px;height:713px}
.about h2,.contact h2{font-size:40px;line-height:46px;font-weight:600;color:var(--heading)}
.about p,.contact p{font-size:14.5px;line-height:23px}
/* Services */
.services{top:1477px;height:816px;background:var(--slate);color:var(--white);text-align:center}
.services h2,.blog h2{font-size:37px;font-weight:600}
.service{position:absolute;top:245px;width:320px}
.service .icon{width:180px;height:180px;border-radius:50%;background:var(--white);margin:0 auto;display:flex;align-items:center;justify-content:center}
.service h3{font-size:26px;font-weight:600;margin-top:22px}
.service p{font-size:14.5px;line-height:23px;margin-top:14px}
/* Testimonials */
.testimonials{top:2293px;height:749px;text-align:center}
.testimonials h2{font-size:38px;font-weight:600;color:var(--heading)}
.card{position:absolute;left:220px;top:230px;width:736px;height:371px;border:1px solid var(--line);border-radius:6px}
.quote{font-family:"Poppins",sans-serif;font-size:16px;line-height:21px;letter-spacing:1.3px;width:620px;margin:0 auto}
/* Blog */
.blog{top:3042px;height:927px;background:var(--slate);color:var(--white);text-align:center}
.post{position:absolute;top:279px;width:300px;text-align:left}
.post .photo{position:static;height:168px;width:300px}
.post h3{font-size:25px;line-height:31px;font-weight:600;margin-top:22px}
.post p{font-size:14.5px;line-height:23px;margin-top:16px}
/* Contact */
.contact{top:3969px;height:615px}
/* Footer */
.footer{top:4584px;height:175px;background:var(--slate);color:var(--white);text-align:center;font-family:"Poppins",sans-serif}
</style>
</head>
<body>

<header class="hero">
  <nav class="nav">
    <a style="left:100px" href="#">Home</a>
    <a style="left:175px" href="#">Leistungen</a>
    <a style="left:288px" href="#">Profil</a>
    <a style="left:362px" href="#">Blog</a>
  </nav>
  <div class="brand-mark">Wohlgemut<br>Coaching</div>
  <span class="social" style="left:804px"></span>
  <span class="social" style="left:863px"></span>
  <span class="social" style="left:922px"></span>
  <div class="btn" style="left:982px;top:102px;width:118px;height:42px">Kontakt</div>

  <div class="abs eyebrow" style="left:100px;top:314px;color:var(--ink)">Für technische Visionäre</div>
  <h1>Coaching,<br>das Sie zum Erfolg führt</h1>
  <p>Beratung für Führungskräfte und Entscheider mit technischem Hintergrund.<br>Mit einer fundierten Expertise in den Bereichen Forschung &amp; Entwicklung, Engineering, Technik, Maschinenbau und Naturwissenschaften stehe ich Ihnen zur Seite, um Ihre beruflichen und persönlichen Herausforderungen zu meistern.</p>
  <div class="btn" style="left:100px;top:607px;width:171px;height:43px">Mehr über mich</div>
  <div class="btn" style="left:288px;top:607px;width:198px;height:43px;background:var(--button-grey)">Termin vereinbaren</div>
  <div class="photo" role="img" aria-label="Porträtfoto des Coaches mit verschränkten Armen in hellblauem Hemd" style="left:757px;top:295px;width:341px;height:469px;background:linear-gradient(180deg,#e9eef0 0%,#b9cfe0 55%,#a7c1d6 100%);border-radius:140px 140px 0 0"></div>
</header>

<section class="about">
  <div class="photo" role="img" aria-label="Runder Bildausschnitt: Coach nachdenklich im Büro" style="left:139px;top:200px;width:332px;height:332px;border-radius:50%;background:radial-gradient(circle at 50% 40%,#d9e3ea 0%,#b4c9d8 60%,#8fa9bb 100%)"></div>
  <div class="abs eyebrow" style="left:535px;top:112px">Christian Wohlgemut</div>
  <h2 class="abs" style="left:535px;top:140px">Profitieren Sie von<br>meiner Expertise</h2>
  <p class="abs" style="left:535px;top:250px;width:530px">Ich bin Christian Wohlgemut, zertifizierter Coach mit einer Leidenschaft für die Entwicklung von Führungskräften und Entscheidern im technischen Bereich. Mit einem Hintergrund in [Fachgebiet] und einer langjährigen Erfahrung in der Unterstützung von Menschen auf ihrem Weg zu persönlichem und beruflichem Wachstum, stehe ich Ihnen als vertrauensvoller Begleiter zur Seite.</p>
  <p class="abs" style="left:535px;top:389px;width:530px">Mein Coaching-Ansatz vereint technische Expertise mit einem tiefen Verständnis für persönliche Entwicklung und Sinnhaftigkeit in der Führung. In unserer Zusammenarbeit schaffen wir einen Raum für Reflexion, Sparring und zielgerichtete Veränderung. Meine Mission ist es, Sie dabei zu unterstützen, nicht nur beruflichen Erfolg zu erzielen, sondern auch eine erfüllende und sinnvolle Führungskraft zu werden.</p>
  <div class="btn" style="left:535px;top:558px;width:327px;height:42px">Erfahren Sie mehr über mein Angebot</div>
</section>

<section class="services">
  <div class="eyebrow" style="position:absolute;top:112px;width:100%">Leistungen</div>
  <h2 style="position:absolute;top:138px;width:100%">Gemeinsam auf Kurs gehen</h2>

  <div class="service" style="left:100px">
    <div class="icon"><svg width="90" height="90" viewBox="0 0 90 90" fill="none" stroke="#7b9faf" stroke-width="2"><circle cx="45" cy="20" r="7"/><path d="M42 28h6M45 6v4M33 12l3 3M57 12l-3 3"/><circle cx="25" cy="45" r="8"/><circle cx="65" cy="45" r="8"/><path d="M11 78v-12a14 14 0 0 1 28 0v12zM51 78v-12a14 14 0 0 1 28 0v12z"/></svg></div>
    <h3>Coaching</h3>
    <p>In meinem Coaching legen wir gemeinsam den Fokus auf bedeutungsvolle Veränderungen in Ihrem Leben und Ihrer beruflichen Laufbahn. Ich unterstütze Sie in den Bereichen Sinn-Coaching, begleite Sie durch Umbrüche und Veränderungen – sei es im privaten oder beruflichen Kontext – und biete Ihnen Sparring und Reflexion auf höchstem Niveau.</p>
  </div>
  <div class="service" style="left:440px">
    <div class="icon"><svg width="90" height="90" viewBox="0 0 90 90" fill="none" stroke="#7b9faf" stroke-width="2"><path d="M22 80V62h10v18M36 80V52h10v28M50 80V42h10v28M64 80V32h10v48"/><path d="M14 80h64"/><circle cx="40" cy="14" r="5"/><path d="M40 20l-4 14 8 6M36 26l-8 4M38 34l-6 8"/><circle cx="68" cy="14" r="6"/><circle cx="68" cy="14" r="2"/></svg></div>
    <h3>Ihr Nutzen</h3>
    <p>Als erfahrener Coach verbinde ich Fachkompetenz mit Einfühlungsvermögen, um Ihnen nicht nur praktische Werkzeuge an die Hand zu geben, sondern auch einen Raum für persönliches Wachstum und Entfaltung zu schaffen. Ihr Erfolg und Ihre Zufriedenheit stehen im Mittelpunkt meiner Arbeit.</p>
  </div>
  <div class="service" style="left:778px">
    <div class="icon"><svg width="90" height="90" viewBox="0 0 90 90" fill="none" stroke="#7b9faf" stroke-width="2"><circle cx="45" cy="22" r="12"/><circle cx="45" cy="40" r="8"/><circle cx="24" cy="46" r="7"/><circle cx="66" cy="46" r="7"/><path d="M31 76v-10a14 14 0 0 1 28 0v10zM12 74v-8a12 12 0 0 1 14-11M78 74v-8a12 12 0 0 0-14-11"/></svg></div>
    <h3>Zielgruppe</h3>
    <p>Meine Dienstleistungen richten sich an Führungskräfte und Entscheider in technischen Disziplinen. Ob Sie in der Forschung tätig sind, im Bereich Engineering, Technik, Maschinenbau oder Naturwissenschaften – ich bin hier, um Sie auf Ihrem Weg zu begleiten.</p>
  </div>
</section>

<section class="testimonials">
  <div class="eyebrow" style="position:absolute;top:112px;width:100%">Testimonials</div>
  <h2 style="position:absolute;top:138px;width:100%">Echte Geschichten, echte Erfahrungen</h2>
  <svg class="abs" style="left:143px;top:2415px;top:392px" width="34" height="60" viewBox="0 0 34 60" fill="none" stroke="#d5d9dc" stroke-width="5"><path d="M30 4L6 30l24 26"/></svg>
  <svg class="abs" style="left:1023px;top:392px" width="34" height="60" viewBox="0 0 34 60" fill="none" stroke="#5e6b73" stroke-width="5"><path d="M4 4l24 26L4 56"/></svg>
  <div class="card">
    <svg style="margin-top:44px" width="264" height="38" viewBox="0 0 264 38" fill="var(--star)">
      <g id="s"><path d="M19 1l5.6 11.4 12.4 1.8-9 8.8 2.1 12.4L19 29.5 7.9 35.4 10 23 1 14.2l12.4-1.8z"/></g>
      <use href="#s" x="56"/><use href="#s" x="112"/><use href="#s" x="168"/><use href="#s" x="224"/>
    </svg>
    <p class="quote" style="margin-top:24px">"Als technische Führungskraft stand ich vor großen Herausforderungen bei der Umsetzung von Veränderungen in unserem Team. Herr Wohlgemut hat mir durch sein einfühlsames Coaching geholfen, nicht nur strategische Lösungen zu finden, sondern auch meine persönliche Führungskompetenz zu stärken."</p>
    <div class="abs" role="img" aria-label="Profilbild des Kunden" style="left:215px;top:268px;width:70px;height:70px;border-radius:50%;background:linear-gradient(180deg,#d8d8d8,#9a9a9a)"></div>
    <div class="abs" style="left:310px;top:280px;text-align:left;font-family:'Poppins',sans-serif">
      <div style="font-size:16px;font-weight:600;color:#4a5157">Jonas Hellwig</div>
      <div style="font-size:13px;color:var(--muted);margin-top:4px">Nordwerk AG</div>
    </div>
  </div>
  <svg class="abs" style="left:572px;top:632px" width="56" height="12"><circle cx="6" cy="6" r="5" fill="#2f3438"/><circle cx="27" cy="6" r="4" fill="#e6e8ea"/><circle cx="47" cy="6" r="4" fill="#e6e8ea"/></svg>
</section>

<section class="blog">
  <div class="eyebrow" style="position:absolute;top:118px;width:100%">Blog</div>
  <h2 style="position:absolute;top:145px;width:100%;line-height:52px">Reflexionen &amp; Erfolgsgeschichten:<br>Der Coaching-Blog</h2>
  <article class="post" style="left:113px">
    <div class="photo" role="img" aria-label="Foto: Führungskraft blickt nachdenklich aus dem Fenster" style="background:linear-gradient(135deg,#eef2f4,#9fa9b0 60%,#3f464c)"></div>
    <h3>Selbstreflexion für Führungskräfte - Kunst und Praxis</h3>
    <p>Tauchen Sie ein in die Kunst der Selbstreflexion und entdecken Sie, warum diese Fähigkeit für technische Führungskräfte so entscheidend ist. Finden Sie praktische Tipps, um diese in Ihren Führungsalltag zu integrieren.</p>
  </article>
  <article class="post" style="left:450px">
    <div class="photo" role="img" aria-label="Foto: Team im Büro mit Glühbirnen-Idee" style="background:linear-gradient(135deg,#f4f2dc,#b7c6d6 55%,#5b6f85)"></div>
    <h3>Innovation und Führung: Kreativität im Management</h3>
    <p>Entdecken Sie, wie Sie Kreativität im technischen Management fördern können: Bewährte Methoden, um eine inspirierende Unternehmenskultur zu schaffen und Innovationen in Ihrem Team zu fördern.</p>
  </article>
  <article class="post" style="left:788px">
    <div class="photo" role="img" aria-label="Foto: Zwei Geschäftsleute mit Boxhandschuhen" style="background:linear-gradient(135deg,#d9d3cf,#b34a42 55%,#3d3a3c)"></div>
    <h3>Die Macht des Sparrings: Führung durch konstruktives Feedback</h3>
    <p>Erfahren Sie, wie Führungskräfte im technischen Bereich durch Sparring wachsen können. Lesen Sie praktische Einblicke, um Ihre Kompetenzen zu verbessern.</p>
  </article>
  <div class="btn" style="left:497px;top:770px;width:206px;height:44px;background:var(--white);color:var(--slate-dark)">Alle Artikel anzeigen</div>
</section>

<section class="contact">
  <div class="abs eyebrow" style="left:138px;top:108px">Bereit für Veränderung?</div>
  <h2 class="abs" style="left:138px;top:136px">Ich bin für Sie da –<br>Schreiben Sie mir!</h2>
  <p class="abs" style="left:138px;top:250px;width:480px">Vereinbaren Sie noch heute Ihr erstes kostenloses Beratungsgespräch und entdecken Sie, wie Coaching Ihr Leben und Ihre berufliche Laufbahn transformieren kann.</p>
  <p class="abs" style="left:138px;top:343px;width:480px">Wenn Sie nach einem engagierten Coach suchen, der Sie in Ihren Zielen unterstützt und Ihnen hilft, Ihr volles Potenzial zu entfalten, nehmen Sie Kontakt auf. Gemeinsam gestalten wir Ihren Weg zu nachhaltigem Erfolg und persönlichem Wohlbefinden.</p>
  <div class="btn" style="left:138px;top:460px;width:202px;height:42px">Kontakt aufnehmen</div>
  <div class="photo" role="img" aria-label="Runder Bildausschnitt: Coach mit verschränkten Armen vor hellem Hintergrund" style="left:722px;top:93px;width:332px;height:332px;border-radius:50%;background:radial-gradient(circle at 50% 35%,#e2e8ec 0%,#b8cde0 60%,#8eaac2 100%)"></div>
  <div class="abs" style="left:722px;top:448px;width:332px;text-align:center;font-size:17px;font-weight:600;color:#4a5157">Christian Wohlgemut</div>
  <div class="abs" style="left:722px;top:476px;width:332px;text-align:center;font-size:14px;letter-spacing:2px;color:var(--slate-dark)">WOHLGEMUT COACHING</div>
</section>

<footer class="footer">
  <div style="position:absolute;top:48px;width:100%;font-size:15px;font-weight:600">Impressum&nbsp;&nbsp;&nbsp;Datenschutz</div>
  <div style="position:absolute;top:100px;width:100%;font-size:14px">© 2024 Christian Wohlgemut Coaching</div>
</footer>

</body>
</html>
```